The Copper Ladder

we require a classy business card design for a business coaching company that uses our current logo and the wording:

Front of card:

LOGO
Kyle Morrison
CEO
TEL: 1300 4 52918
FAX: 1300 5 52918
Mobile: 0412 638194
PO Box 917, Ferris Hollow, Brisbane, Qld 4127
e: kylem@copperladder.com.au
w: www.copperladder.com.au

Reverse side of the card:

Systematizing Businesses into Turnkey Operations
Strategic Business Plans
Sales & Marketing Programs
Sales Training & Business Coaching
Internet Marketing & Web Design

Here’s what our clients say:

“We grew from $396,000 to over $5million in 4 years and made KTS’s Rising Enterprises Roll 3 years running!” – Martin Greaves, Meridian Works

Target Market(s)

small to medium sized business owners in Australia

Industry/Entity Type

Business

Requirements
Must have
• standard business card size

```html
<!DOCTYPE html>
<html lang="en">
<head>
<meta charset="utf-8">
<title>The Copper Ladder – Business Card</title>
<link rel="stylesheet" href="https://fonts.googleapis.com/css2?family=Questrial&family=Audiowide&display=swap">
<style>
  :root {
    --page: #ffffff;
    --ink: #1a1a1a;
    --frame: #6b6b6b;
    --gold: #f7b514;
    --gold-soft: #fbd670;
    --name: #f39a12;
  }
  * { margin: 0; padding: 0; box-sizing: border-box; }
  html, body { width: 848px; height: 1200px; overflow: hidden; background: var(--page); }
  body { position: relative; font-family: "Questrial", "Century Gothic", sans-serif; color: var(--ink); }

  .card {
    position: absolute;
    left: 238px;
    width: 356px;
    height: 217px;
    border: 0.8px solid var(--frame);
    background: var(--page);
    overflow: hidden;
  }
  .card--front { top: 395px; }
  .card--back { top: 633px; }

  .stripe {
    position: absolute;
    left: 0; right: 0;
    height: 3px;
    background: linear-gradient(90deg, var(--gold) 0%, var(--gold-soft) 30%, #fff8e6 50%, var(--gold-soft) 70%, var(--gold) 100%);
  }
  .band {
    position: absolute;
    left: 0; right: 0; bottom: 0;
    background: radial-gradient(ellipse 52% 130% at 50% 50%, #ffffff 0%, #fef3d4 30%, var(--gold-soft) 65%, var(--gold) 100%);
  }
  .card--front .stripe { top: 168px; }
  .card--front .band { top: 173px; }
  .card--back .stripe { top: 167px; }
  .card--back .band { top: 171px; }

  .brand {
    position: absolute;
    left: 13px; top: 18px;
    font-size: 14px;
    color: var(--ink);
    letter-spacing: 0.2px;
  }

  .address {
    position: absolute;
    left: 10px; top: 62px;
    font-size: 10.4px;
    line-height: 14px;
    list-style: none;
  }

  .person { position: absolute; left: 224px; top: 75px; }
  .person__name {
    font-family: "Audiowide", sans-serif;
    font-size: 13.5px;
    color: var(--name);
    letter-spacing: 0.6px;
    line-height: 16px;
  }
  .person__role { font-size: 10.4px; line-height: 14px; margin-top: 1px; }

  .band__text {
    position: absolute;
    top: 189px;
    font-size: 9.6px;
    line-height: 12px;
    z-index: 1;
  }
  .band__text--email { left: 10px; }
  .band__text--web { right: 8px; }

  .services {
    position: absolute;
    left: 12px; top: 22px;
    list-style: none;
    font-size: 10.2px;
    line-height: 14px;
  }
  .services li { position: relative; padding-left: 22px; }
  .services li::before {
    content: "•";
    position: absolute;
    left: 0;
    font-size: 9px;
  }

  .testimonial-lead {
    position: absolute;
    left: 9px; top: 148px;
    font-size: 8.4px;
  }
  .testimonial {
    position: absolute;
    left: 9px; top: 177px;
    right: 20px;
    font-size: 8.6px;
    line-height: 14px;
    z-index: 1;
  }
</style>
</head>
<body>

  <section class="card card--front" aria-label="Business card front">
    <div class="brand">The Copper Ladder</div>

    <ul class="address">
      <li>PO Box 917,</li>
      <li>Ferris Hollow,</li>
      <li>Brisbane, Qld 4127</li>
      <li>TEL: 1300 4 52918</li>
      <li>FAX: 1300 5 52918</li>
      <li>Mobile: 0412 638194</li>
    </ul>

    <div class="person">
      <div class="person__name">Kyle Morrison</div>
      <div class="person__role">CEO</div>
    </div>

    <div class="stripe"></div>
    <div class="band"></div>
    <div class="band__text band__text--email">E-mail: kylem@copperladder.com.au</div>
    <div class="band__text band__text--web">Website: www.copperladder.com.au</div>
  </section>

  <section class="card card--back" aria-label="Business card back">
    <ul class="services">
      <li>Systematizing Businesses into Turnkey Operations</li>
      <li>Strategic Business Plans</li>
      <li>Sales &amp; Marketing Programs</li>
      <li>Sales Training &amp; Business Coaching</li>
      <li>Internet Marketing &amp; Web Design</li>
    </ul>

    <p class="testimonial-lead">Here’s what our clients say:</p>

    <div class="stripe"></div>
    <div class="band"></div>
    <p class="testimonial">“We grew from $396,000 to over $5million in 4 years and made KTS’s Rising Enterprises Roll 3 years running!” – Martin Greaves, Meridian Works</p>
  </section>

</body>
</html>
```